Create lumora book cover: Step Aside

I need a cover designed for my book
Title is “Step Aside”
Tag line is “ The Venture Horizon Plan“

With the words “ A handbook on how to remove yourself from your company“ somewhere on the page.

Author name “Neil Corbett”

The cover will be used on lumora and paper back and needs to comply with all RVS formatting rules.

Target Market(s)

Small Business owners

Font styles to use
Serif

```html
<!DOCTYPE html>
<html lang="en">
<head>
<meta charset="utf-8">
<title>Step Aside – Book Cover</title>
<link rel="stylesheet" href="https://fonts.googleapis.com/css2?family=Playfair+Display:ital,wght@0,400;0,500;0,600;0,700;0,900;1,400&display=swap">
<style>
  :root {
    --stage-gold: #c29a41;
    --cover-sky: #e8eef8;
    --cover-sky-deep: #d6e0f0;
    --navy: #0f1a52;
    --ink: #1c1c24;
    --gold-light: #f3d77e;
    --gold-mid: #d4a93a;
    --gold-dark: #a97d1f;
    --photo-blue: #3d5f9a;
    --photo-blue-soft: #9fb4d6;
  }
  * { margin: 0; padding: 0; box-sizing: border-box; }
  html, body {
    width: 1200px;
    height: 722px;
    overflow: hidden;
    background: var(--stage-gold);
  }
  .stage {
    position: relative;
    width: 1200px;
    height: 722px;
    display: flex;
    justify-content: center;
  }
  .cover {
    position: relative;
    width: 481px;
    height: 722px;
    overflow: hidden;
    background: linear-gradient(180deg, var(--cover-sky) 0%, #eef2f9 40%, var(--cover-sky-deep) 100%);
    font-family: "Playfair Display", Georgia, serif;
  }
  .cover-photo {
    position: absolute;
    left: 0;
    top: 250px;
    width: 481px;
    height: 398px;
    background:
      radial-gradient(ellipse 60% 75% at 72% 78%, var(--photo-blue) 0%, rgba(61,95,154,0.55) 45%, rgba(61,95,154,0) 75%),
      linear-gradient(180deg, rgba(159,180,214,0) 0%, rgba(159,180,214,0.45) 100%);
  }
  .title {
    position: absolute;
    left: 0;
    width: 100%;
    text-align: center;
    line-height: 1;
    display: block;
  }
  .title-top {
    top: 18px;
    font-size: 96px;
    font-weight: 400;
    background: linear-gradient(90deg, var(--gold-dark), var(--gold-light) 45%, var(--gold-mid) 70%, var(--gold-dark));
    -webkit-background-clip: text;
    background-clip: text;
    color: transparent;
    letter-spacing: -1px;
  }
  .title-main {
    top: 112px;
    font-size: 104px;
    font-weight: 900;
    color: var(--navy);
    letter-spacing: -2px;
  }
  .tagline {
    position: absolute;
    top: 214px;
    width: 100%;
    text-align: center;
    font-style: italic;
    font-size: 24px;
    line-height: 1.1;
    color: var(--ink);
  }
  .seal {
    position: absolute;
    left: 180px;
    top: 264px;
    width: 136px;
    height: 136px;
    border-radius: 50%;
    background: radial-gradient(circle at 40% 35%, var(--gold-light) 0%, var(--gold-mid) 60%, var(--gold-dark) 100%);
    display: flex;
    flex-direction: column;
    align-items: center;
    justify-content: center;
    text-align: center;
  }
  .seal-rule {
    width: 28px;
    height: 1.5px;
    background: var(--ink);
  }
  .seal-text {
    margin: 8px 0;
    font-size: 13px;
    font-weight: 600;
    line-height: 1.45;
    color: var(--ink);
  }
  .author-band {
    position: absolute;
    left: 0;
    bottom: 0;
    width: 100%;
    height: 76px;
    background: var(--navy);
    border-top: 4px solid var(--gold-mid);
    display: flex;
    align-items: center;
    justify-content: center;
  }
  .author-name {
    font-size: 44px;
    font-weight: 400;
    line-height: 1.1;
    background: linear-gradient(90deg, var(--gold-dark), var(--gold-light) 50%, var(--gold-mid));
    -webkit-background-clip: text;
    background-clip: text;
    color: transparent;
  }
</style>
</head>
<body>
  <main class="stage">
    <section class="cover">
      <div class="cover-photo" role="img" aria-label="Blue-toned double exposure of a cheering businessman in a suit with a raised fist, blended with a city skyline"></div>
      <h1>
        <span class="title title-top">Step</span>
        <span class="title title-main">Aside</span>
      </h1>
      <p class="tagline">The Venture Horizon Plan</p>
      <div class="seal">
        <span class="seal-rule"></span>
        <p class="seal-text">A handbook<br>on how to remove<br>yourself from<br>your company</p>
        <span class="seal-rule"></span>
      </div>
      <footer class="author-band">
        <p class="author-name">Neil Corbett</p>
      </footer>
    </section>
  </main>
</body>
</html>
```